TealFathom.com Website design needed!!

We are looking for a website layout to match the attached logo. We specialize in Dive Charters and currently are located in the Virgin Islands off of Harbor Point. Please create a design that is compatible with Bootstrap and have the grid in mind. WE are looking for creative and extremely professional layout design.

Target Market(s)

Scuba Diving, Divers looking for a diving charter in the Virgin Islands.

Number of Pages Required

3 page

Font styles to use
Serif

Requirements
Must have
• Must be Bootstrap friendly.
• Must work with the logo we provided. Colors etc.

```html
<!DOCTYPE html>
<html lang="en">
<head>
<meta charset="utf-8">
<title>Teal Fathom — Charters and Scuba</title>
<link href="https://fonts.googleapis.com/css2?family=Cinzel:wght@400;700&family=Open+Sans:wght@400;600&display=swap" rel="stylesheet">
<style>
:root{
  --red:#ed1c24;
  --navy:#0b2a6b;
  --ink:#1f1f1f;
  --grey-text:#7a7a7a;
  --panel:#efefef;
  --bar:#4a4d56;
  --white:#ffffff;
  --card-line:#d6d6d6;
}
*{box-sizing:border-box;margin:0;padding:0}
html,body{width:768px;height:1200px;overflow:hidden}
body{position:relative;font-family:"Open Sans",Arial,sans-serif;background:var(--white);color:var(--ink)}
.abs{position:absolute}

/* header */
.site-header{left:0;top:0;width:768px;height:67px;background:var(--white)}
.brand{left:32px;top:20px;display:flex;align-items:center;gap:6px;font-family:"Cinzel",serif;font-weight:700;font-size:17px;color:var(--red)}
.brand-mark{width:12px;height:12px;border-radius:50%;background:var(--navy)}
.brand-sub{left:48px;top:43px;font-family:"Cinzel",serif;font-weight:700;font-size:7px;letter-spacing:1.5px;color:var(--navy)}
.nav{left:269px;top:0;height:67px;display:flex;font-size:6.5px;text-transform:uppercase}
.nav a{display:flex;align-items:center;padding:0 12px;color:var(--navy);text-decoration:none;margin-right:10px}
.nav a.active{background:var(--red);color:var(--white);margin-right:10px}
.call{left:634px;top:21px;display:flex;align-items:center;gap:7px}
.call-label{font-size:7px;color:var(--red);line-height:1}
.call-num{font-size:9.5px;font-weight:600;color:#444}

/* hero */
.hero{left:0;top:67px;width:768px;height:317px;background:radial-gradient(ellipse at 50% 40%,#1d3f8a 0%,#0e2461 55%,#06123a 100%)}
.hero-title{left:0;top:106px;width:768px;text-align:center;font-family:"Cinzel",serif;font-size:29px;color:var(--white);letter-spacing:.5px}
.hero-title b{font-weight:700}
.hero-text{left:138px;top:155px;width:492px;text-align:center;font-size:7.4px;line-height:14.4px;color:var(--white)}
.btn{display:flex;align-items:center;justify-content:center;background:var(--red);color:var(--white);font-size:7px;text-transform:uppercase}
.hero-btn{left:324px;top:208px;width:80px;height:24px;border:1px solid #ff6b6b}
.dots{left:342px;top:273px;display:flex;gap:5px}
.dots span{width:10px;height:10px;border-radius:50%;border:1px solid var(--white)}
.dots span.on{background:var(--red)}

/* search bar */
.search{left:0;top:384px;width:768px;height:57px;background:var(--bar)}
.search-title{left:37px;top:12px;font-family:"Cinzel",serif;font-size:13.5px;line-height:16px;color:var(--white)}
.search-title em{font-style:normal;color:var(--red)}
.field{border:1px solid #8a8d95;color:#d7d8da;font-size:7px;display:flex;align-items:center;padding-left:9px}
.select{left:226px;top:14px;width:163px;height:30px}
.select svg{position:absolute;right:8px;top:12px}
.f-name{left:398px;top:14px;width:114px;height:30px}
.f-email{left:521px;top:14px;width:113px;height:30px}
.find-btn{left:663px;top:12px;width:75px;height:33px;border:1px solid #ff8a8a;font-family:"Cinzel",serif;font-weight:700;font-size:8px;line-height:10px;text-align:center}

/* welcome */
.welcome{left:0;top:441px;width:768px;height:180px;background:var(--panel)}
.rule{height:1px;background:#d2d2d2}
.welcome-title,.news-title{left:0;width:768px;text-align:center;font-family:"Cinzel",serif;font-weight:700;font-size:19px;color:var(--ink)}
.welcome-title span,.news-title span{color:var(--red)}
.welcome-text{left:64px;top:75px;width:640px;text-align:center;font-size:7.2px;line-height:13.6px;color:var(--grey-text)}
.welcome-btn{left:338px;top:125px;width:91px;height:30px}

/* news */
.news{left:0;top:621px;width:768px;height:193px}
.card{top:79px;width:230px;height:74px;border:1px solid var(--card-line);background:var(--white)}
.card-img{position:absolute;left:6px;top:12px;width:60px;height:47px}
.card-title{position:absolute;left:79px;top:12px;font-family:"Cinzel",serif;font-weight:700;font-size:7.5px;color:var(--red)}
.card-text{position:absolute;left:79px;top:25px;width:145px;font-size:7px;line-height:13.4px;color:var(--grey-text)}
.card-more{position:absolute;left:80px;top:52px;font-size:7px;color:var(--ink);display:flex;align-items:center;gap:3px}

/* get started */
.started{left:0;top:814px;width:768px;height:337px;background:linear-gradient(120deg,#2c2c2c 0%,#4b4644 45%,#3a3837 70%,#262626 100%)}
.started-title{left:47px;top:62px;font-family:"Cinzel",serif;font-size:19px;color:var(--white)}
.started-text{left:48px;top:94px;width:315px;font-size:7.2px;line-height:13.4px;color:var(--white)}
.started-rule{left:48px;top:144px;width:313px;height:1px;background:#a9a9a9}
.address{left:51px;top:160px;font-size:9.4px;line-height:18.2px;color:var(--white)}
.address .gap{height:18px}
.input{left:420px;width:311px;height:23px;border:1px solid #b3b3b3;background:rgba(255,255,255,.08);color:var(--white);font-size:9.4px;padding:3px 9px}
.send{left:645px;top:286px;width:86px;height:27px;font-size:12px}

/* footer */
.footer{left:0;top:1151px;width:768px;height:49px;background:var(--red)}
.copy{left:0;top:19px;width:768px;text-align:center;font-size:6.5px;font-weight:600;color:var(--white)}
.social{left:641px;top:14px;display:flex;gap:6px}
.social span{width:19px;height:18px;border:1px solid var(--white)}
.social span.fill{background:var(--white)}
</style>
</head>
<body>

<header class="abs site-header">
  <div class="abs brand"><span class="brand-mark"></span>Teal Fathom</div>
  <div class="abs brand-sub">HARBOR POINT</div>
  <nav class="abs nav">
    <a class="active" href="#">Teal Fathom</a>
    <a href="#">About Us</a>
    <a href="#">Contact</a>
    <a href="#">Learn More</a>
    <a href="#">Schedule</a>
  </nav>
  <div class="abs call">
    <svg width="26" height="26" viewBox="0 0 26 26">
      <circle cx="13" cy="13" r="12" fill="none" stroke="#ed1c24" stroke-width="1"/>
      <path d="M9.5 8.5c.8-.6 1.6-.5 2 .2l.8 1.5c.3.6.1 1.1-.4 1.5l-.5.4c.6 1.4 1.6 2.4 3 3l.4-.5c.4-.5 1-.7 1.5-.4l1.5.8c.7.4.8 1.2.2 2-.8 1-2 1.3-3.2.8-2.8-1.1-4.8-3.1-5.9-5.9-.5-1.2-.2-2.4.6-3.4z" fill="#ed1c24"/>
      <path d="M15 7.5a4 4 0 0 1 3.5 3.5M15 5.5a6 6 0 0 1 5.5 5.5" fill="none" stroke="#ed1c24" stroke-width=".9"/>
    </svg>
    <div><div class="call-label">CALL US</div><div class="call-num">+123-456-7890</div></div>
  </div>
</header>

<section class="abs hero" role="img" aria-label="Two scuba divers in masks swimming in deep blue water">
  <h1 class="abs hero-title"><b>Teal Fathom</b> Charters and Scuba</h1>
  <p class="abs hero-text">Lorem ipsum dolor sit amet, consectetur adipiscing elit, sed do eiusmod tempor incididunt ut labore et dolore magna aliqua. Ut enim ad minim veniam, quis nostrud exercitation ullamco laboris nisi ut aliquip ex ea commodo consequat. Duis aute irure dolor in reprehenderit in voluptate velit esse cillum dolore eu fugiat nulla pariatur.</p>
  <a class="abs btn hero-btn">Read More</a>
  <div class="abs dots"><span class="on"></span><span></span><span></span></div>
</section>

<section class="abs search">
  <h2 class="abs search-title">Search for your dream<br>charter <em>today!</em></h2>
  <div class="abs field select">I have approximate dates
    <svg width="8" height="5" viewBox="0 0 8 5"><path d="M0 0h8L4 5z" fill="#fff"/></svg>
  </div>
  <div class="abs field f-name">Name</div>
  <div class="abs field f-email">Email id</div>
  <a class="abs btn find-btn">Find<br>Charters</a>
</section>

<section class="abs welcome">
  <div class="abs rule" style="left:30px;top:42px;width:175px"></div>
  <div class="abs rule" style="left:567px;top:42px;width:169px"></div>
  <h2 class="abs welcome-title" style="top:30px">Welcome to <span>Teal Fathom</span></h2>
  <p class="abs welcome-text">Lorem ipsum dolor sit amet, consectetur adipiscing elit, sed do eiusmod tempor incididunt ut labore et dolore magna aliqua. Ut enim ad minim veniam, quis nostrud exercitation ullamco laboris nisi ut aliquip ex ea commodo consequat. Duis aute irure dolor in reprehenderit in voluptate velit esse cillum dolore eu fugiat nulla pariatur. Excepteur sint occaecat cupidatat non proident, sunt in culpa qui officia deserunt mollit anim id est laborum.</p>
  <a class="abs btn welcome-btn">Read More</a>
</section>

<section class="abs news">
  <h2 class="abs news-title" style="top:27px">Latest <span>News</span></h2>
  <article class="abs card" style="left:30px">
    <div class="card-img" role="img" aria-label="Diver beside a colourful coral reef" style="background:linear-gradient(135deg,#c9762a,#2c5b6e 60%,#123447)"></div>
    <h3 class="card-title">This is a test title</h3>
    <p class="card-text">Lorem ipsum dolor sit amet, consectetur adipiscing elit, sed do eiusmod tempor</p>
    <span class="card-more">READ MORE <svg width="4" height="6" viewBox="0 0 4 6"><path d="M0 0l4 3-4 3z" fill="#1f1f1f"/></svg></span>
  </article>
  <article class="abs card" style="left:269px">
    <div class="card-img" role="img" aria-label="Diver wearing a yellow mask underwater" style="background:linear-gradient(135deg,#4fa3d6,#1f6aa0 60%,#0e3a63)"></div>
    <h3 class="card-title">This is a test title</h3>
    <p class="card-text">Lorem ipsum dolor sit amet, consectetur adipiscing elit, sed do eiusmod tempor</p>
    <span class="card-more">READ MORE <svg width="4" height="6" viewBox="0 0 4 6"><path d="M0 0l4 3-4 3z" fill="#1f1f1f"/></svg></span>
  </article>
  <article class="abs card" style="left:507px">
    <div class="card-img" role="img" aria-label="Lionfish swimming over the reef" style="background:linear-gradient(135deg,#2f88a8,#3a3a3a 55%,#1c4e66)"></div>
    <h3 class="card-title">This is a test title</h3>
    <p class="card-text">Lorem ipsum dolor sit amet, consectetur adipiscing elit, sed do eiusmod tempor</p>
    <span class="card-more">READ MORE <svg width="4" height="6" viewBox="0 0 4 6"><path d="M0 0l4 3-4 3z" fill="#1f1f1f"/></svg></span>
  </article>
</section>

<section class="abs started" role="img" aria-label="Dimmed close-up of a hand touching a screen">
  <h2 class="abs started-title">Get Started</h2>
  <p class="abs started-text">Lorem ipsum dolor sit amet, consectetur adipiscing elit, sed do eiusmod tempor incididunt ut labore et dolore magna aliqua. Ut enim ad minim veniam, quis nostrud exercitation ullamco laboris nisi ut aliquip ex ea commodo consequat.</p>
  <div class="abs started-rule"></div>
  <div class="abs address">
    <div>123 Address line1, Address line 2</div>
    <div>Country, 123456.</div>
    <div>Freephone: +1 234 567 890</div>
    <div>Telephone: +1 234 567 890</div>
    <div>FAX: +1 504 889 9898</div>
    <div class="gap"></div>
    <div>E-mail: mail@Companyname.org</div>
  </div>
  <div class="abs input" style="top:96px">Name</div>
  <div class="abs input" style="top:139px">Email id</div>
  <div class="abs input" style="top:181px">Phone</div>
  <div class="abs input" style="top:220px;height:55px">Address</div>
  <a class="abs btn send">SEND</a>
</section>

<footer class="abs footer">
  <p class="abs copy">Copyright 2016 Company Name. All Rights Reserved.</p>
  <div class="abs social"><span></span><span></span><span class="fill"></span><span></span></div>
</footer>

</body>
</html>
```